Bref créative
Wedding photographer business card
and stationary
Bright & Fun-filled
Lora Bexley
no address needed
lorabexley@mailvista.net
www.lorabexley.net
I like sleek but also fun and feminine.
corrected phone number given to winning designer for finalizing design.
Thanks
Special offer,
$50 off,
a package & a free 8x10 print
I have two designs so you may choose either logo to design.
here's the monogram for my second logo
the flowers for logo 2

```html
<!DOCTYPE html>
<html lang="en">
<head>
<meta charset="utf-8">
<title>Lora Bexley – Folded Card Proposal</title>
<link rel="stylesheet" href="https://fonts.googleapis.com/css2?family=Great+Vibes&family=Cormorant+Garamond:wght@500;600;700&family=Cinzel:wght@400;600&display=swap">
<style>
  :root{
    --page:#ffffff;
    --charcoal:#4b4542;
    --cream:#fbf8e9;
    --rose:#e9707c;
    --rose-soft:#f29aa2;
    --ink:#3a3532;
    --label-bar:#d9d9d9;
    --label-ink:#5a5a5a;
    --light:#f5f1ea;
  }
  *{margin:0;padding:0;box-sizing:border-box}
  html,body{width:1200px;height:989px;overflow:hidden;background:var(--page)}
  .sheet{position:relative;width:1200px;height:989px}
  .proposal-title{
    position:absolute;left:259px;top:27px;width:906px;height:52px;
    background:var(--label-bar);color:var(--label-ink);
    font:600 22px/52px "Cormorant Garamond",serif;letter-spacing:3px;text-align:center;
  }
  .panel{position:absolute;overflow:hidden}
  .panel-dark{background:var(--charcoal);color:var(--light)}
  .panel-cream{background:var(--cream)}
  .outside-back{left:59px;top:160px;width:533px;height:333px}
  .outside-front{left:592px;top:160px;width:531px;height:333px}
  .inside-left{left:59px;top:568px;width:533px;height:331px;
    background:radial-gradient(ellipse at 45% 60%,#f0a0ad 0%,#d9788a 28%,#7f8a4c 55%,#9a7b58 75%,#c9c3b4 100%)}
  .inside-right{left:592px;top:568px;width:531px;height:331px}
  .panel-label{position:absolute;font:600 20px "Cormorant Garamond",serif;letter-spacing:2px;color:var(--ink)}
  .offer{position:absolute;inset:0;display:flex;flex-direction:column;align-items:center;justify-content:center;text-align:center}
  .offer-script{font:400 50px "Great Vibes",cursive;color:var(--rose);line-height:1;transform:rotate(-4deg);margin-bottom:6px}
  .offer-amount{font:600 34px "Cormorant Garamond",serif;color:var(--light);line-height:1.1}
  .offer-detail{font:600 30px "Cormorant Garamond",serif;color:var(--light);line-height:1.1}
  .brand-front{position:absolute;inset:0;display:flex;align-items:center;justify-content:center;gap:18px}
  .brand-dot{width:22px;height:22px;border-radius:50%;background:var(--rose)}
  .brand-name{font:400 74px "Great Vibes",cursive;color:var(--ink)}
  .inside-content{position:absolute;inset:0;display:flex;flex-direction:column;align-items:center;padding-top:42px}
  .inside-name{font:400 70px "Great Vibes",cursive;color:var(--light);line-height:1.1}
  .inside-role{font:400 17px "Cinzel",serif;letter-spacing:4px;color:var(--light);margin-top:8px}
  .inside-rule{width:370px;height:2px;background:var(--light);margin:18px 0 24px}
  .contact-row{display:flex;align-items:center;gap:10px;font:400 17px "Cinzel",serif;color:var(--light);letter-spacing:1px}
  .contact-row+.contact-row{margin-top:16px}
  .contact-group{display:flex;align-items:center;gap:8px}
  .contact-row svg{flex:none}
  .web{letter-spacing:5px}
</style>
</head>
<body>
<div class="sheet">
  <div class="proposal-title">2X3.5 FOLDED CARD DESIGN PROPOSAL { PRINT OPTIONS AVAILABLE }</div>

  <section class="panel panel-dark outside-back">
    <div class="offer">
      <div class="offer-script">Special offer</div>
      <div class="offer-amount">$50.00 OFF</div>
      <div class="offer-detail">A PACKAGE &amp; A</div>
      <div class="offer-detail">FREE 8X10 PRINT</div>
    </div>
  </section>

  <section class="panel panel-cream outside-front">
    <div class="brand-front">
      <span class="brand-dot"></span>
      <span class="brand-name">Lora Bexley</span>
    </div>
  </section>

  <div class="panel-label" style="left:59px;top:515px">OUTSIDE BACK</div>
  <div class="panel-label" style="right:77px;top:515px">OUTSIDE FRONT</div>

  <section class="panel inside-left" role="img" aria-label="Photo of a bridal bouquet of pink tulips and white roses on a windowsill"></section>

  <section class="panel panel-dark inside-right">
    <div class="inside-content">
      <div class="inside-name">Lora Bexley</div>
      <div class="inside-role">WEDDING PHOTOGRAPHER</div>
      <div class="inside-rule"></div>
      <div class="contact-row">
        <span class="contact-group">
          <svg width="16" height="16" viewBox="0 0 24 24"><path fill="var(--rose)" d="M6.6 10.8a15 15 0 0 0 6.6 6.6l2.2-2.2c.3-.3.7-.4 1-.2 1.1.4 2.3.6 3.6.6.6 0 1 .4 1 1V20c0 .6-.4 1-1 1A17 17 0 0 1 3 4c0-.6.4-1 1-1h3.5c.6 0 1 .4 1 1 0 1.3.2 2.5.6 3.6.1.3 0 .7-.2 1z"/></svg>
          813-555-0142
        </span>
        <span class="contact-group" style="margin-left:14px">
          <svg width="20" height="14" viewBox="0 0 20 14"><rect x="1" y="1" width="18" height="12" fill="none" stroke="var(--rose)" stroke-width="1.6"/><path d="M1 1l9 7 9-7" fill="none" stroke="var(--rose)" stroke-width="1.6"/></svg>
          LORABEXLEY@MAILVISTA.NET
        </span>
      </div>
      <div class="contact-row">
        <svg width="18" height="18" viewBox="0 0 20 20"><circle cx="10" cy="10" r="8.5" fill="none" stroke="var(--rose)" stroke-width="1.6"/><ellipse cx="10" cy="10" rx="3.8" ry="8.5" fill="none" stroke="var(--rose)" stroke-width="1.3"/><path d="M1.5 10h17M3 6h14M3 14h14" stroke="var(--rose)" stroke-width="1.2"/></svg>
        <span class="web">WWW.LORABEXLEY.NET</span>
      </div>
    </div>
  </section>

  <div class="panel-label" style="left:59px;top:921px">INSIDE LEFT</div>
  <div class="panel-label" style="right:77px;top:921px">INSIDE RIGHT</div>
</div>
</body>
</html>
```